Corvanta512 Business Card Redesign

I want to create a design for brand new business cards, I need something exceptional for clear plastic business card design. Please do not submit without it being on a clear design. Photos of the various logo versions attached.

```html
<!DOCTYPE html>
<html lang="en">
<head>
<meta charset="utf-8">
<title>Corvanta512 Clear Business Card</title>
<link href="https://fonts.googleapis.com/css2?family=Montserrat:wght@400;500;700&display=swap" rel="stylesheet">
<style>
  :root {
    --page-bg: #e9e3da;
    --card-clear-a: #f4f1ec;
    --card-clear-b: #dfe3e6;
    --card-edge: rgba(255,255,255,0.8);
    --navy: #283a55;
    --gold: #c9a23e;
    --gold-text: #c8a44a;
    --ink: #2e2e33;
  }
  * { margin: 0; padding: 0; box-sizing: border-box; }
  html, body { width: 1200px; height: 897px; overflow: hidden; }
  body {
    background: var(--page-bg);
    font-family: "Montserrat", Arial, sans-serif;
    position: relative;
  }
  .card {
    position: absolute;
    left: 80px; top: 164px;
    width: 1040px; height: 568px;
    border-radius: 22px;
    overflow: hidden;
    background: linear-gradient(120deg, var(--card-clear-a) 0%, var(--card-clear-b) 55%, var(--card-clear-a) 100%);
    border: 1px solid var(--card-edge);
    box-shadow: 0 10px 30px rgba(60,50,40,0.18);
  }
  .card__bands { position: absolute; inset: 0; width: 100%; height: 100%; }
  .brand {
    position: absolute; left: 57px; top: 192px;
    display: flex; align-items: center; gap: 14px;
  }
  .brand__dot {
    width: 26px; height: 26px; border-radius: 50%;
    background: var(--navy);
  }
  .brand__name {
    font-size: 36px; font-weight: 700; color: var(--gold-text);
    letter-spacing: 0.5px;
  }
  .name-bar {
    position: absolute; left: 3px; top: 273px;
    width: 23px; height: 55px; background: var(--navy);
  }
  .person {
    position: absolute; left: 55px; top: 268px;
  }
  .person__name {
    font-size: 32px; font-weight: 700; color: var(--gold-text);
    letter-spacing: 1px; line-height: 38px;
  }
  .person__title {
    font-size: 23px; font-weight: 500; color: var(--ink); line-height: 28px;
  }
  .address {
    position: absolute; left: 55px; top: 352px;
    font-size: 22px; color: var(--ink); line-height: 32px; letter-spacing: 0.5px;
  }
  .contacts {
    position: absolute; left: 55px; top: 424px;
    list-style: none;
    font-size: 22px; color: var(--ink); letter-spacing: 0.5px;
  }
  .contacts li {
    display: flex; align-items: center; gap: 10px; height: 35px;
  }
  .contacts svg { width: 18px; height: 18px; fill: var(--ink); flex: none; }
</style>
</head>
<body>
  <div class="card">
    <svg class="card__bands" viewBox="0 0 1040 568" aria-hidden="true">
      <defs>
        <linearGradient id="band" x1="0" y1="0" x2="0" y2="1">
          <stop offset="0" stop-color="#283a55"/>
          <stop offset="0.5" stop-color="#283a55"/>
          <stop offset="0.5" stop-color="#c9a23e"/>
          <stop offset="1" stop-color="#d6b45a"/>
        </linearGradient>
      </defs>
      <path d="M760,0 L1040,0 L1040,568 L760,568 C900,560 1000,520 1005,440 L1010,170 C1010,60 900,10 760,0 Z" fill="url(#band)"/>
    </svg>

    <div class="brand">
      <span class="brand__dot"></span>
      <span class="brand__name">Corvanta512</span>
    </div>

    <div class="name-bar"></div>
    <div class="person">
      <p class="person__name">DELAN MARKEY</p>
      <p class="person__title">CEO/Founder</p>
    </div>

    <p class="address">4170 Harbor Lane<br>Westfield AB 60318</p>

    <ul class="contacts">
      <li>
        <svg viewBox="0 0 24 24"><path d="M6.6 10.8a15.1 15.1 0 0 0 6.6 6.6l2.2-2.2a1 1 0 0 1 1-.25 11.4 11.4 0 0 0 3.6.57 1 1 0 0 1 1 1V20a1 1 0 0 1-1 1A17 17 0 0 1 3 4a1 1 0 0 1 1-1h3.5a1 1 0 0 1 1 1c0 1.25.2 2.45.57 3.57a1 1 0 0 1-.25 1z"/></svg>
        <span>(555) 310 482</span>
      </li>
      <li>
        <svg viewBox="0 0 24 24"><path d="M2 5h20v14H2z M2 5l10 8 10-8" fill="none" stroke="#2e2e33" stroke-width="2"/></svg>
        <span>info@corvanta512.com</span>
      </li>
      <li>
        <svg viewBox="0 0 24 24"><circle cx="12" cy="12" r="9" fill="none" stroke="#2e2e33" stroke-width="2"/><path d="M3 12h18M12 3c3 3 3 15 0 18M12 3c-3 3-3 15 0 18" fill="none" stroke="#2e2e33" stroke-width="1.6"/></svg>
        <span>www.corvanta512.com</span>
      </li>
    </ul>
  </div>
</body>
</html>
```